Simple and Clean business card design

We would like the design to be simple clean and to incorporate our colors.

We are open to your design and talent, we have the dots in our logo as we think of it as data points and we connect data points for people.

We are open to see the great creative and clean design you bring to the table

Contact Information for Business Card

please include: name, position, email, phone and website

Font styles to use
Sans Serif

Requirements
Must have
• my colors incorporated, simplicity
Nice to have
• lots of white space, simplicity
Should not have
• complexicity/ complex art

```html
<!DOCTYPE html>
<html lang="en">
<head>
<meta charset="UTF-8">
<title>Nectra Business Card</title>
<link rel="stylesheet" href="https://fonts.googleapis.com/css2?family=Open+Sans:wght@400;600&family=Rajdhani:wght@700&display=swap">
<style>
  :root {
    --page: #fdfdfd;
    --ink: #000000;
    --text: #1e1e1e;
    --paper: #ffffff;
    --brand-blue: #4285f4;
    --frame: #222222;
  }
  html, body {
    margin: 0;
    width: 1200px;
    height: 1200px;
    overflow: hidden;
    background: var(--page);
    font-family: "Open Sans", sans-serif;
  }
  .card {
    position: absolute;
    left: 216px;
    width: 775px;
    height: 430px;
    box-sizing: border-box;
  }
  .card-front {
    top: 148px;
    background: var(--ink);
  }
  .card-back {
    top: 630px;
    background: var(--paper);
    border: 1px solid var(--frame);
  }
  .wordmark {
    position: absolute;
    left: 0;
    right: 0;
    display: flex;
    justify-content: center;
    align-items: baseline;
    gap: 10px;
    font-weight: 600;
    letter-spacing: 1px;
    line-height: 1;
  }
  .wordmark-dot {
    display: inline-block;
    border-radius: 50%;
  }
  .card-front .wordmark {
    top: 165px;
    font-size: 100px;
    color: var(--paper);
  }
  .card-front .wordmark-dot {
    width: 22px;
    height: 22px;
    background: var(--paper);
  }
  .card-back .wordmark {
    top: 52px;
    font-size: 112px;
    color: var(--ink);
  }
  .card-back .wordmark-dot {
    width: 25px;
    height: 25px;
    background: var(--brand-blue);
  }
  .rule {
    position: absolute;
    top: 202px;
    left: 27px;
    width: 722px;
    height: 2px;
    background: linear-gradient(to right, rgba(0,0,0,0), rgba(0,0,0,0.85) 50%, rgba(0,0,0,0));
  }
  .identity {
    position: absolute;
    top: 256px;
    right: 448px;
    text-align: right;
    font-family: "Rajdhani", sans-serif;
    font-weight: 700;
    line-height: 1;
  }
  .identity-name {
    font-size: 42px;
    color: var(--brand-blue);
    letter-spacing: 1.5px;
  }
  .identity-role {
    margin-top: 4px;
    font-size: 23px;
    color: var(--ink);
    letter-spacing: 1.5px;
  }
  .separator {
    position: absolute;
    left: 381px;
    top: 250px;
    width: 2px;
    height: 89px;
    background: var(--frame);
  }
  .contacts {
    position: absolute;
    left: 420px;
    top: 244px;
    margin: 0;
    padding: 0;
    list-style: none;
  }
  .contact-item {
    display: flex;
    align-items: center;
    height: 33px;
    font-size: 21px;
    color: var(--text);
  }
  .contact-icon {
    width: 28px;
    height: 28px;
    margin-right: 15px;
    flex: none;
  }
  .address {
    position: absolute;
    left: 0;
    right: 0;
    top: 375px;
    text-align: center;
    font-size: 21px;
    color: var(--text);
  }
</style>
</head>
<body>
  <section class="card card-front">
    <div class="wordmark"><span>Nectra</span><span class="wordmark-dot"></span></div>
  </section>

  <section class="card card-back">
    <div class="wordmark"><span>Nectra</span><span class="wordmark-dot"></span></div>
    <div class="rule"></div>

    <div class="identity">
      <div class="identity-name">LIAM CORDER</div>
      <div class="identity-role">CEO/FOUNDER</div>
    </div>

    <div class="separator"></div>

    <ul class="contacts">
      <li class="contact-item">
        <svg class="contact-icon" viewBox="0 0 24 24" aria-hidden="true">
          <path fill="#4285f4" d="M6.6 2.5c.5-.4 1.2-.3 1.5.2l1.6 2.6c.3.5.2 1.1-.2 1.5l-1.1 1c.9 2.6 2.7 4.8 5 6.3l1.2-.9c.5-.3 1.1-.3 1.5.1l2.2 2.1c.4.4.5 1.1.1 1.6l-1 1.2c-.6.7-1.6.9-2.4.5C9.6 16.4 6 12 4.6 6.6c-.2-.8.1-1.7.8-2.2z"/>
        </svg>
        <span>555-214-3098</span>
      </li>
      <li class="contact-item">
        <svg class="contact-icon" viewBox="0 0 24 24" aria-hidden="true" fill="none" stroke="#4285f4" stroke-width="1.3">
          <circle cx="12" cy="12" r="10"/>
          <ellipse cx="12" cy="12" rx="4.5" ry="10"/>
          <line x1="12" y1="2" x2="12" y2="22"/>
          <line x1="2" y1="12" x2="22" y2="12"/>
          <path d="M4 7h16M4 17h16"/>
        </svg>
        <span>www.nectra.one</span>
      </li>
      <li class="contact-item">
        <svg class="contact-icon" viewBox="0 0 24 24" aria-hidden="true">
          <rect x="2" y="5" width="20" height="14" fill="#4285f4"/>
          <path d="M2.5 5.5 12 13l9.5-7.5M2.5 18.5 9.5 11.5M21.5 18.5 14.5 11.5" fill="none" stroke="#ffffff" stroke-width="1.2"/>
        </svg>
        <span>liam.corder@nectra.one</span>
      </li>
    </ul>

    <div class="address">Address line goes here, street name, country name</div>
  </section>
</body>
</html>
```